Mortgage Broking boutique Business

I’m wanting a revamped look to my existing business card design. I do like the black and silver but happy to have other colours introduced based on your creation. I’ve attached a copy of my current card so you can have a starting point updated details noted brloe. I deal with high net worth individuals so need my card to be sophisticated, classy that gives off a classy vibe

Target Market(s)

High net worth, wealthy

Industry/Entity Type

Mortgage Brokerage

Contact Information for Business Card

Job title: Finance Executive
Phone: +61 7 3287 4419
Mobile: 0471 352 608
Email: marcus@quillbrookcapital.com.au
Web: www.quillbrookcapital.com.au
Address: level 36 Tindale Court, 58 Harwick St Brisbane QLD 4000

Font styles to use
Other font styles liked:
• Helvetica

Colors

Designer to choose colors to be used in the design.

Requirements
Must have
• Use my existing card design as a starting point

```html
<!DOCTYPE html>
<html lang="en">
<head>
<meta charset="utf-8">
<title>Quillbrook Capital – Business Card</title>
<link href="https://fonts.googleapis.com/css2?family=Jost:wght@400;500;600&display=swap" rel="stylesheet">
<style>
  :root {
    --backdrop: #4b4c4c;
    --card: #1c1c1c;
    --silver: #c9c9c9;
    --silver-soft: #a9a9a9;
    --name-grey: #8c8c8c;
    --text: #e2e2e2;
  }
  * { margin: 0; padding: 0; box-sizing: border-box; }
  html, body {
    width: 963px; height: 1200px; overflow: hidden;
    background: var(--backdrop);
    font-family: "Jost", "Futura", sans-serif;
  }
  .stage { position: relative; width: 963px; height: 1200px; }
  .card {
    position: absolute; left: 203px; width: 556px; height: 318px;
    background: var(--card);
  }
  .card--front { top: 220px; }
  .card--back { top: 636px; }

  .frame {
    position: absolute; inset: 20px;
    border: 1px solid var(--silver);
  }

  .holder { position: absolute; left: 36px; top: 62px; }
  .holder__name {
    font-size: 22px; font-weight: 600; color: var(--name-grey);
    letter-spacing: 0.2px; line-height: 1;
  }
  .holder__title {
    margin-top: 6px; font-size: 14px; color: var(--text); font-weight: 400;
  }

  .address {
    position: absolute; left: 38px; top: 126px;
    font-size: 13.5px; line-height: 16.5px; color: var(--text);
    font-style: normal;
  }

  .contacts {
    position: absolute; left: 38px; top: 188px; list-style: none;
    font-size: 13.5px; color: var(--text);
  }
  .contacts li { display: flex; align-items: center; height: 17.5px; }
  .contacts svg { width: 11px; height: 11px; margin-right: 9px; fill: var(--silver-soft); flex: none; }

  .wordmark {
    position: absolute; text-align: center; color: var(--silver);
    font-weight: 500; text-transform: uppercase; line-height: 1;
  }
  .card--front .wordmark { left: 300px; width: 240px; top: 132px; }
  .card--front .wordmark__main { font-size: 22px; letter-spacing: 4px; }
  .card--front .wordmark__sub { font-size: 13px; letter-spacing: 3.5px; margin-top: 7px; }

  .seal {
    position: absolute; left: 139px; top: 90px; width: 278px; height: 142px;
    border: 1.5px solid var(--silver);
  }
  .seal::after {
    content: ""; position: absolute; inset: 4px;
    border: 1.5px solid var(--silver);
  }
  .card--back .wordmark { left: 0; right: 0; top: 58px; }
  .card--back .wordmark__main { font-size: 15px; letter-spacing: 2.5px; }
  .card--back .wordmark__sub { font-size: 9px; letter-spacing: 2.5px; margin-top: 5px; }
</style>
</head>
<body>
<main class="stage">
  <section class="card card--front">
    <div class="frame"></div>
    <div class="holder">
      <h1 class="holder__name">MARCUS REID</h1>
      <p class="holder__title">Finance Executive</p>
    </div>
    <address class="address">
      level 36 Tindale Court<br>
      58 Harwick St<br>
      Brisbane QLD 4000
    </address>
    <ul class="contacts">
      <li><svg viewBox="0 0 12 12"><path d="M2.5 0.5l2 2.2-1 1.3c.7 1.5 1.9 2.7 3.5 3.5l1.3-1 2.2 2-1.4 2C5 10.3 1.7 7 0.5 1.9z"/></svg>+61 7 3287 4419</li>
      <li><svg viewBox="0 0 12 12"><path d="M3 0h6v12H3zM4 1.5v8h4v-8z"/></svg>0471 352 608</li>
      <li><svg viewBox="0 0 12 12"><path d="M0 2.5h12v7H0zM1 3.3l5 3.5 5-3.5v-.3H1z"/></svg>marcus@quillbrookcapital.com.au</li>
      <li><svg viewBox="0 0 12 12"><circle cx="6" cy="6" r="5.5"/></svg>www.quillbrookcapital.com.au</li>
    </ul>
    <div class="wordmark">
      <div class="wordmark__main">Quillbrook</div>
      <div class="wordmark__sub">Capital</div>
    </div>
  </section>

  <section class="card card--back">
    <div class="seal">
      <div class="wordmark">
        <div class="wordmark__main">Quillbrook</div>
        <div class="wordmark__sub">Capital</div>
      </div>
    </div>
  </section>
</main>
</body>
</html>
```